Indie musician needs album cover art

I am an independant musician releasing my second album via digital sources. I plan to make it available on Vendly and other digital stores but primarily distribute it free through Tunegrove.

The album's music style is a blend of singer-songwriter folk, punk, alt country, electronic rock and spoken word. The lyrical content is a dark journey through travel in foreign countries, relationships, airports and theatres, formed during my own journey as an audio engineer for a travelling theatre show.

The album is called "Ash Under Glass" - at times both a plea and a directive. I would like the album cover to reflect a sense of longing, restlessness, unease and movement. A subversive tone is also possible.

I have had a go at designing a couple of ideas myself, using my own photos. I like the ideas but I am not skilled in graphic design and am unable to take them further to get the right feel and look. I will post these as examples of tone. The finished work does not need to copy either of these.

A .zip of the album can be downloaded here (low fi mp3):

http://fylo.io/Qx7rT4

Target Market(s)

People who enjoy thoughtful, honest, homemade music. Definitely not a teeny pop audience. Adult, subversive, educated, emotional...

Industry/Entity Type

Graphic Design

Requirements
Must have
• Artist name (no caps): kipwren
Album name (prefer no caps): ash under glass

```html
<!DOCTYPE html>
<html lang="en">
<head>
<meta charset="utf-8">
<title>kipwren – ash under glass</title>
<link rel="stylesheet" href="https://fonts.googleapis.com/css2?family=Quicksand:wght@300;700&display=swap">
<style>
  :root {
    --page: #ffffff;
    --night-top: #1f2230;
    --night-mid: #34302e;
    --lamp-amber: #b8742c;
    --ride-yellow: #b9a83c;
    --ground: #4a4a52;
    --title: #ffffff;
    --band: rgba(38, 34, 48, 0.82);
    --band-text: #e9e4dc;
  }
  html, body {
    margin: 0;
    padding: 0;
    width: 1200px;
    height: 900px;
    overflow: hidden;
    background: var(--page);
  }
  .canvas {
    position: relative;
    width: 1200px;
    height: 900px;
    background: var(--page);
  }
  .album-cover {
    position: absolute;
    left: 260px;
    top: 110px;
    width: 681px;
    height: 681px;
    overflow: hidden;
  }
  .cover-photo {
    position: absolute;
    inset: 0;
    background:
      radial-gradient(circle at 12% 22%, rgba(214, 110, 40, 0.55) 0 6%, transparent 14%),
      radial-gradient(circle at 95% 18%, rgba(190, 120, 70, 0.6) 0 8%, transparent 20%),
      radial-gradient(ellipse at 80% 60%, rgba(185, 168, 60, 0.75) 0 18%, transparent 38%),
      radial-gradient(ellipse at 25% 56%, rgba(170, 110, 130, 0.55) 0 12%, transparent 28%),
      radial-gradient(ellipse at 55% 85%, rgba(200, 130, 40, 0.55) 0 10%, transparent 24%),
      linear-gradient(180deg, var(--night-top) 0%, var(--night-mid) 45%, var(--ground) 100%);
  }
  .artist-name {
    position: absolute;
    left: 0;
    right: 0;
    top: 278px;
    margin: 0;
    text-align: center;
    font-family: "Quicksand", sans-serif;
    font-weight: 700;
    font-size: 112px;
    line-height: 1;
    letter-spacing: -2px;
    color: var(--title);
  }
  .album-title {
    position: absolute;
    left: 97px;
    top: 550px;
    width: 480px;
    height: 65px;
    margin: 0;
    background: var(--band);
    display: flex;
    align-items: center;
    justify-content: center;
    font-family: "Quicksand", sans-serif;
    font-weight: 300;
    font-size: 40px;
    letter-spacing: 6px;
    color: var(--band-text);
  }
</style>
</head>
<body>
  <main class="canvas">
    <section class="album-cover">
      <div class="cover-photo" role="img" aria-label="Night-time snapshot of a fairground ride with glowing amber lights and a yellow ride car"></div>
      <h1 class="artist-name">kipwren</h1>
      <h2 class="album-title">ash under glass</h2>
    </section>
  </main>
</body>
</html>
```